Bright Path Flyer Design for Virtual Online Clinic. -5.5 x 8.5 inches (half sheet)

We need a clean, modern flyer design for Bright Path, a new virtual walk-in clinic based in British Columbia. The flyer will be used in libraries, pharmacies, and community centers to help residents easily access primary care through their Bright Path NFC access card.
The flyer will ask a question : NEED A DOCTOR? This should be large and attention grabbing.
The design should clearly feature a Bright Path card image (the access card) as the centerpiece and visually show how patients can use it to book appointments. The tone should feel trustworthy, healthcare-oriented, and community-friendly — clean fonts, clear spacing, and strong readability from a distance.

Side One: This card has the NFC Access Card.
NEED A DOCTOR? (Large Font, Attention Grabbing)
How to Book an Appointment using your Bright Path Card
Step 1: Tap Your Card on Your Phone
Hold your card near the back of your phone.
It will activate automatically — no app needed.
The Bright Path scheduler will open.
Step 2: Schedule Your Appointment
Select your clinical concern.
Choose your time window.
Register (only once).
Confirm your appointment.
Step 3: Relax, we’ll take care of the rest
A doctor will call during your scheduled time.
Once booked, you’ll be able to call our office.
No emails, no texts — just a real person.
It’s that simple.
Side Two:
About Bright Path
Created by Dr. Marcus Ferrigan
Bright Path was founded to make healthcare simple and convenient. Prescription renewals. Common infections. Medical notes. And so much more.
Our doctors can address 120+ health concerns virtually — providing quality care without the waiting room. No waiting rooms. Just real doctors providing real care.
Why Patients Choose Bright Path
Easy access – book and be seen from anywhere in BC.
Effortless booking – tap your Bright Path Card to begin.
Trusted physicians – every visit is with a licensed BC family doctor.
How It Works
Book your visit — choose a time window that fits your day.
Join the queue — you’ll be called when it’s your turn.
Speak directly with your doctor — simple, secure, and stress-free.
Convenient Care for Common Concerns

Additional Details.
Please find the domain to be launched soon. I've attached the NFC card file for review, it is 85.5 mm x 54 mm. The card will be glued to the flyer.
I've attached examples of flyers but they are not the look I am seeking and I am looking for creative solutions.
Thank you!
http://brightpath-example.test/

Adult Patients in British Columbia

Healthcare

• Looking for clean lines, uniform appearance, and high legibility i.e poppins

0054AA
0677BA
7BADD7
CADEEF
E8F1F8

• Need A Doctor?
• Elegant style, not too busy, clear layout.
• Clutter, look cheap - review examples.

```html
<!DOCTYPE html>
<html lang="en">
<head>
<meta charset="utf-8">
<title>Bright Path Flyer – Front and Back</title>
<link rel="stylesheet" href="https://fonts.googleapis.com/css2?family=Poppins:wght@300;400;500;600;700;800&family=Playball&display=swap">
<style>
  :root {
    --navy: #27408b;
    --navy-deep: #223a85;
    --brand-blue: #0677ba;
    --step-blue: #0a8fd8;
    --step-head: #9dd6f5;
    --sky: #a8d8f5;
    --pale: #e8f1f8;
    --white: #ffffff;
    --canvas: #eeeeee;
    --ink: #1f2a44;
  }
  * { box-sizing: border-box; margin: 0; padding: 0; }
  html, body { width: 1200px; height: 1200px; overflow: hidden; }
  body { background: var(--canvas); font-family: "Poppins", sans-serif; position: relative; }

  .flyer { position: absolute; top: 271px; width: 489px; height: 695px; overflow: hidden; box-shadow: 0 1px 4px rgba(0,0,0,.12); }
  .flyer--front { left: 79px; background: var(--white); }
  .flyer--back { left: 623px; background: linear-gradient(180deg, #0a7fc8 0%, #1d5fb0 35%, #2a4493 65%, #2a4493 100%); color: var(--white); }

  .abs { position: absolute; }

  /* Front */
  .front-photo { left: 0; top: 0; width: 489px; height: 290px; background: linear-gradient(160deg, #dbe9f4 0%, #c6dced 40%, #e8f1f8 70%, #cfe0ee 100%); }
  .front-shapes { left: 0; top: 0; }
  .welcome { left: 0; width: 489px; top: 34px; text-align: center; font-weight: 700; font-size: 27px; color: var(--navy); letter-spacing: -.2px; }
  .access-card { left: 99px; top: 84px; width: 291px; height: 183px; background: var(--white); border: 6px solid var(--navy); border-radius: 12px; display: flex; align-items: center; justify-content: center; }
  .access-card .brand-name { font-size: 24px; font-weight: 500; color: var(--navy); }
  .book-title { left: 0; width: 489px; top: 282px; text-align: center; color: var(--white); font-weight: 700; font-size: 26px; line-height: 33px; letter-spacing: -.2px; }

  .step { top: 373px; width: 134px; height: 228px; border-radius: 12px; background: var(--step-blue); overflow: hidden; color: var(--white); text-align: center; }
  .step__head { height: 39px; background: var(--step-head); color: var(--navy); font-weight: 700; font-size: 25px; line-height: 39px; }
  .step__title { font-weight: 700; font-size: 13px; line-height: 16px; margin: 13px 4px 10px; }
  .step__line { font-size: 10.5px; line-height: 12px; font-weight: 400; padding: 0 6px 5px; }
  .step__rule { height: 1px; margin: 0 12px 5px; background: rgba(255,255,255,.35); }

  .help { left: 28px; top: 615px; width: 270px; font-size: 10px; line-height: 15px; color: var(--ink); }
  .help strong { display: block; color: var(--navy); font-size: 13.5px; font-weight: 700; margin-top: 2px; }
  .front-brand { left: 318px; top: 622px; font-size: 22px; font-weight: 500; color: var(--navy); }
  .front-bar { left: 27px; top: 686px; width: 434px; height: 10px; background: var(--navy); }

  /* Back */
  .section-head { left: 25px; width: 430px; display: flex; align-items: center; gap: 4px; font-size: 20.5px; font-weight: 400; color: var(--sky); white-space: nowrap; }
  .section-head::after { content: ""; flex: 1; height: 1px; background: var(--sky); margin-top: 10px; }
  .about-text { left: 25px; top: 76px; width: 431px; font-size: 12px; line-height: 16px; text-align: justify; }
  .about-text p + p { margin-top: 16px; }
  .why-col { top: 270px; }
  .why-col__top { display: flex; align-items: center; gap: 9px; height: 40px; }
  .why-col__title { font-weight: 700; font-size: 13.5px; line-height: 15px; }
  .why-col__text { margin-top: 10px; font-size: 12px; line-height: 17px; font-weight: 400; }
  .how-item { top: 423px; display: flex; gap: 8px; }
  .how-item svg { flex: none; }
  .how-item__title { font-weight: 700; font-size: 13.5px; line-height: 15px; }
  .how-item__text { font-size: 10.5px; line-height: 13px; margin-top: 2px; }
  .back-photo { left: 0; top: 0; }
  .back-brand { left: 0; width: 489px; top: 586px; text-align: center; font-size: 26px; font-weight: 500; }
  .tagline { left: 0; width: 489px; top: 628px; text-align: center; font-family: "Playball", cursive; font-size: 24px; }
  .site { left: 0; width: 489px; top: 658px; text-align: center; font-size: 16px; font-weight: 400; }
</style>
</head>
<body>

<!-- Front side -->
<section class="flyer flyer--front">
  <div class="abs front-photo" role="img" aria-label="Soft-focus photo of a doctor in a white coat with laboratory glassware"></div>
  <svg class="abs front-shapes" width="489" height="695" viewBox="0 0 489 695" aria-hidden="true">
    <path d="M120 215 C250 160 380 145 489 158 L489 190 C360 176 240 200 0 275 L0 268 C40 245 80 228 120 215 Z" fill="#ffffff"/>
    <path d="M0 275 C120 205 300 170 489 190 L489 573 L0 573 Z" fill="#27408b"/>
  </svg>
  <h1 class="abs welcome">Welcome To Bright Path</h1>
  <div class="abs access-card"><span class="brand-name">Bright Path</span></div>
  <h2 class="abs book-title">How to Book an Appointment<br>using your Bright Path Card</h2>

  <article class="abs step" style="left:28px">
    <div class="step__head">Step 1</div>
    <div class="step__title">Tap Your Card<br>on Your Phone</div>
    <p class="step__line">Hold your card near the back of your phone.</p>
    <div class="step__rule"></div>
    <p class="step__line">It will activate automatically —<br>no app needed.</p>
    <div class="step__rule"></div>
    <p class="step__line">The Bright Path scheduler will open.</p>
  </article>

  <article class="abs step" style="left:177px">
    <div class="step__head">Step 2</div>
    <div class="step__title">Schedule Your<br>Appointment</div>
    <p class="step__line">Select your clinical concern.</p>
    <div class="step__rule"></div>
    <p class="step__line">Choose your time window.</p>
    <div class="step__rule"></div>
    <p class="step__line">Register (only once).</p>
    <div class="step__rule"></div>
    <p class="step__line">Confirm your appointment.</p>
  </article>

  <article class="abs step" style="left:327px">
    <div class="step__head">Step 3</div>
    <div class="step__title">Relax, we’ll take<br>care of the rest</div>
    <p class="step__line">A doctor will call during your scheduled time.</p>
    <div class="step__rule"></div>
    <p class="step__line">Once booked, you’ll be able to call our office.</p>
    <div class="step__rule"></div>
    <p class="step__line">No emails, no texts —<br>just a real person.</p>
  </article>

  <p class="abs help">If you’re having trouble with your card or the access page, we’re her to help:<strong>support@brightpath-example.test</strong></p>
  <div class="abs front-brand">Bright Path</div>
  <div class="abs front-bar"></div>
</section>

<!-- Back side -->
<section class="flyer flyer--back">
  <h2 class="abs section-head" style="top:36px">About Bright Path</h2>
  <div class="abs about-text">
    <p>Created by Dr. Marcus Ferrigan<br>Bright Path was founded to make healthcare simple and convenient. Prescription renewals. Common infections. Medical notes. And so much more.</p>
    <p>Our doctors can address 120+ health concerns virtually — providing quality care without the waiting room. No waiting rooms. Just real doctors providing real care.</p>
  </div>

  <h2 class="abs section-head" style="top:229px">Why Patients Choose Bright Path</h2>

  <div class="abs why-col" style="left:25px">
    <div class="why-col__top">
      <svg width="24" height="34" viewBox="0 0 24 34" fill="none" stroke="#fff" stroke-width="1.4" stroke-linecap="round" stroke-linejoin="round" aria-hidden="true">
        <path d="M8 20 V9 a2 2 0 0 1 4 0 V18 M12 16 a2 2 0 0 1 4 0 v3 M16 18 a2 2 0 0 1 4 0 v5 c0 6-4 9-8 9 c-4 0-7-3-8-6 l-2-5 a2 2 0 0 1 3-2 l3 3"/>
        <path d="M6 4 l2 3 M12 1 v4 M18 4 l-2 3"/>
      </svg>
      <div class="why-col__title">Easy<br>access</div>
    </div>
    <p class="why-col__text">book and be seen<br>from anywhere in BC.</p>
  </div>

  <div class="abs why-col" style="left:168px">
    <div class="why-col__top">
      <svg width="24" height="34" viewBox="0 0 24 34" fill="none" stroke="#fff" stroke-width="1.4" stroke-linecap="round" stroke-linejoin="round" aria-hidden="true">
        <path d="M3 6 h18 v26 H3 Z M8 6 V3 h8 v3"/>
        <path d="M8 19 l3 3 l6-7"/>
      </svg>
      <div class="why-col__title">Effortless<br>booking</div>
    </div>
    <p class="why-col__text">tap your Bright Path<br>Card to begin.</p>
  </div>

  <div class="abs why-col" style="left:315px">
    <div class="why-col__top">
      <svg width="30" height="34" viewBox="0 0 30 34" fill="none" stroke="#fff" stroke-width="1.4" stroke-linecap="round" stroke-linejoin="round" aria-hidden="true">
        <circle cx="15" cy="9" r="6"/>
        <path d="M3 32 v-6 c0-5 5-8 12-8 s12 3 12 8 v6"/>
        <path d="M15 18 v8 M10 19 v5 a3 3 0 0 0 6 0"/>
      </svg>
      <div class="why-col__title">Trusted<br>physicians</div>
    </div>
    <p class="why-col__text">every visit is with a<br>licensed BC family doctor.</p>
  </div>

  <h2 class="abs section-head" style="top:378px;left:24px;width:431px">How It Works</h2>

  <div class="abs how-item" style="left:25px">
    <svg width="17" height="52" viewBox="0 0 17 52" aria-hidden="true"><path d="M0 0 L17 26 L0 52 Z" fill="#7badd7"/></svg>
    <div><div class="how-item__title">Book your visit</div><p class="how-item__text">choose a time window<br>that fits your day.</p></div>
  </div>
  <div class="abs how-item" style="left:177px">
    <svg width="17" height="52" viewBox="0 0 17 52" aria-hidden="true"><path d="M0 0 L17 26 L0 52 Z" fill="#7badd7"/></svg>
    <div><div class="how-item__title">Join the queue</div><p class="how-item__text">you’ll be called<br>when it’s your turn</p></div>
  </div>
  <div class="abs how-item" style="left:313px">
    <svg width="17" height="52" viewBox="0 0 17 52" aria-hidden="true"><path d="M0 0 L17 26 L0 52 Z" fill="#7badd7"/></svg>
    <div><div class="how-item__title">Speak directly<br>with your doctor</div><p class="how-item__text">simple, secure, and<br>stress-free.</p></div>
  </div>

  <svg class="abs back-photo" width="489" height="695" viewBox="0 0 489 695" role="img" aria-label="Photo of a clinician gently holding a patient's hands">
    <defs>
      <linearGradient id="photoTone" x1="0" y1="0" x2="1" y2="1">
        <stop offset="0" stop-color="#5f86bd"/>
        <stop offset=".45" stop-color="#3f65a8"/>
        <stop offset="1" stop-color="#233f8c"/>
      </linearGradient>
      <linearGradient id="swoosh" x1="0" y1="0" x2="1" y2="0">
        <stop offset="0" stop-color="#ffffff" stop-opacity="0"/>
        <stop offset="1" stop-color="#ffffff" stop-opacity=".95"/>
      </linearGradient>
    </defs>
    <path d="M0 555 C150 530 350 525 489 466 L489 695 L0 695 Z" fill="url(#photoTone)"/>
    <path d="M110 530 C270 522 400 500 489 459 L489 466 C380 518 240 540 0 555 L0 548 Z" fill="url(#swoosh)"/>
  </svg>

  <div class="abs back-brand">Bright Path</div>
  <div class="abs tagline">Convenient Care for Common Concerns</div>
  <div class="abs site">www.brightpath-example.test</div>
</section>

</body>
</html>
```